Lumina+ Parlour Product Package Designs

We are currently launching a new spa, beauty and cosmetic product line called Lumina+ Parlour.

Our products ranging from pumice stones, sponges, and bath straps to cosmetic products.

There are four packaging label/product tags (please see attached templates as well as samples)

It needs to include:
Barcode placeholder
Product name placeholder
Area for brief product description (2-4 sentences)
website www.luminaplusparlour.example

Target Market(s)

end consumers (85% female)

Industry/Entity Type

Boutique

Font styles to use
Sans Serif
Decorative
Script

Colors
ffffff
e34197
e667a6
eda3c7
f9d9e8
fbd4d5
b768aa
d2a4cc

Requirements
Must have
• - Logo should be pink (do not modify the colour - shade can change slightly)
• - All four packaging designs should be combined into a single submission

```html
<!DOCTYPE html>
<html lang="en">
<head>
<meta charset="utf-8">
<title>Lumina+ Parlour – Turmeric Powder Bag Layout</title>
<link rel="stylesheet" href="https://fonts.googleapis.com/css2?family=Arimo:wght@400;700&family=Barlow:wght@400;600&family=Pathway+Gothic+One&display=swap">
<style>
  :root {
    --paper: #ffffff;
    --bag-light: #fdf5c4;
    --bag-warm: #fbdd9c;
    --band: rgba(250, 190, 100, 0.55);
    --panel: rgba(250, 190, 95, 0.6);
    --halo: rgba(255, 250, 215, 0.55);
    --guide: #e0203a;
    --safe-zone: #d4d4d4;
    --ink: #111111;
    --ink-soft: #222222;
  }
  * { margin: 0; padding: 0; box-sizing: border-box; }
  html, body { width: 1200px; height: 698px; overflow: hidden; background: var(--paper); }
  .sheet { position: relative; width: 1200px; height: 698px; font-family: "Arimo", Arial, sans-serif; color: var(--ink); }

  .size-title { position: absolute; left: 28px; width: 460px; top: 52px; text-align: center; font-size: 38px; font-weight: 400; }

  .bag { position: absolute; top: 104px; width: 400px; height: 534px; }
  .bag--front { left: 30px; }
  .bag--back { left: 598px; }
  .bag__pattern { position: absolute; inset: 0; background: linear-gradient(135deg, var(--bag-light) 0%, var(--bag-warm) 45%, var(--bag-light) 70%, var(--bag-warm) 100%); }
  .bag__trim { position: absolute; left: 14px; top: 10px; width: 370px; height: 515px; border: 1px solid var(--guide); }
  .bag__hanger { position: absolute; left: 50%; top: 42px; transform: translateX(-50%); }
  .bag__safe-zone { position: absolute; left: 8px; right: 10px; top: 88px; height: 20px; background: var(--safe-zone); border-top: 1px solid var(--guide); border-bottom: 1px solid var(--guide); font-size: 7.5px; text-align: center; line-height: 18px; }
  .bag__caption { position: absolute; top: 641px; width: 400px; text-align: center; font-weight: 700; font-size: 14px; }

  .brand-halo { position: absolute; left: 84px; top: 132px; width: 232px; height: 232px; border-radius: 50%; background: var(--halo); display: flex; align-items: center; justify-content: center; }
  .brand-name { font-family: "Barlow", sans-serif; font-weight: 600; font-size: 30px; color: var(--ink); }

  .product-band { position: absolute; left: 0; top: 378px; width: 401px; height: 60px; background: var(--band); display: flex; align-items: center; justify-content: center; }
  .product-name { font-family: "Barlow", sans-serif; font-weight: 600; font-size: 30px; letter-spacing: 0.5px; }

  .info-panel { position: absolute; left: 34px; top: 122px; width: 328px; height: 392px; background: var(--panel); font-family: "Pathway Gothic One", sans-serif; color: var(--ink-soft); }
  .info-panel h2 { position: absolute; left: 42px; font-weight: 400; font-size: 14px; }
  .info-panel .copy { position: absolute; left: 42px; width: 260px; font-size: 12.8px; line-height: 16.8px; text-align: justify; }
  .maker { position: absolute; left: 43px; top: 268px; font-size: 15.5px; line-height: 19.2px; }
  .barcode-slot { position: absolute; left: 176px; top: 272px; width: 140px; height: 78px; background: var(--paper); }
  .web { position: absolute; left: 43px; top: 364px; font-size: 15.5px; }

  .dimensions { position: absolute; inset: 0; pointer-events: none; }
  .dim-label { position: absolute; font-size: 24px; }
</style>
</head>
<body>
<main class="sheet">
  <h1 class="size-title">129x180mm</h1>

  <section class="bag bag--front">
    <div class="bag__pattern" role="img" aria-label="Soft yellow and orange gingham check pattern"></div>
    <div class="bag__trim"></div>
    <svg class="bag__hanger" width="82" height="26" viewBox="0 0 82 26"><path d="M12 9 H32 A9 8 0 0 1 50 9 H70 A10 8.5 0 0 1 70 25 H12 A10 8.5 0 0 1 12 9 Z" fill="none" stroke="#e0203a" stroke-width="1"/></svg>
    <div class="bag__safe-zone">NO TEXT IN THIS AREA</div>
    <div class="brand-halo"><span class="brand-name">Lumina+ Parlour</span></div>
    <div class="product-band"><span class="product-name">TURMERIC POWDER</span></div>
  </section>
  <p class="bag__caption" style="left:30px">Plastic Bag - Front</p>

  <section class="bag bag--back">
    <div class="bag__pattern" role="img" aria-label="Soft yellow and orange gingham check pattern"></div>
    <div class="bag__trim"></div>
    <svg class="bag__hanger" width="72" height="26" viewBox="0 0 72 26"><path d="M10 9 H27 A9 8 0 0 1 45 9 H62 A9 8.5 0 0 1 62 25 H10 A9 8.5 0 0 1 10 9 Z" fill="none" stroke="#e0203a" stroke-width="1"/></svg>
    <div class="bag__safe-zone">NO TEXT IN THIS AREA</div>
    <div class="info-panel">
      <h2 style="top:26px">PRODUCT DESCRIPTION</h2>
      <p class="copy" style="top:47px">Lorem ipsum dolor sit amet, consectetur adipiscing elit. Morbi ultricies molestie orci. Aenean purus mauris, sodales nec diam dignissim, porttitor laoreet enim.</p>
      <h2 style="top:108px">INSTRUCTIONS</h2>
      <p class="copy" style="top:129px">Aliquam id sollicitudin turpis. Vivamus aliquet elit sem, et ornare ex aliquam in. In cursus, felis non pretium molestie, tellus lacus facilisis metus, ut accumsan nisi nulla accumsan risus.</p>
      <h2 style="top:204px">MATERIALS</h2>
      <p class="copy" style="top:225px">Nunc sit amet ante id justo consequat tempor.</p>
      <p class="maker">Manufactured in China<br>and distributed by:<br>Lumina Plus Parlour<br>Maple Bay, Northland</p>
      <div class="barcode-slot" role="img" aria-label="Barcode placeholder"></div>
      <p class="web">www.luminaplusparlour.example</p>
    </div>
  </section>
  <p class="bag__caption" style="left:598px">Plastic Bag - Back</p>

  <svg class="dimensions" width="1200" height="698" viewBox="0 0 1200 698" fill="none" stroke="#e0203a" stroke-width="1">
    <path d="M613 64 H982 M613 58 V104 M982 58 V104"/>
    <path d="M982 114 H1134 M1019 114 V330 M1019 410 V629 M1088 114 V629 M997 629 H1088"/>
    <path d="M982 196 H1026 M982 209 H1026"/>
  </svg>
  <span class="dim-label" style="left:754px;top:34px;background:#fff;padding:0 4px">129mm</span>
  <span class="dim-label" style="left:1104px;top:120px">1.5cm</span>
  <span class="dim-label" style="left:1000px;top:142px">3cm</span>
  <span class="dim-label" style="left:997px;top:186px">0.5cm</span>
  <span class="dim-label" style="left:1088px;top:354px;transform:rotate(-90deg)">180mm</span>
</main>
</body>
</html>
```